Biz Card for Marla Dempsey Insurance Agency
Biz Card for Marla Dempsey Insurance Agency - Financial Services
Creative Brief
Bright & Fun-filled
Marla Dempsey
Independent Agent
Ashford, TN
office 336-521-0974
cell 336-597-2160
marladempsey34@qorvinmail.com
please include her picture in her new card. I will also upload a copy of what we are currently using. she needs something new and fresh. please use the new logo we upload.
Also, please see the words we are using for the back of her card, please use those same words on the new cards.

```html
<!DOCTYPE html>
<html lang="en">
<head>
<meta charset="utf-8">
<title>Marla Dempsey Insurance Agency – Business Cards</title>
<link rel="stylesheet" href="https://fonts.googleapis.com/css2?family=Cinzel:wght@400;600;700&display=swap">
<style>
  :root {
    --page-bg: #e6e8eb;
    --card-white: #ffffff;
    --navy: #1d3a64;
    --band-grey: #8593a3;
    --band-grey-dark: #5f6d7d;
    --brand-green: #3d8a2f;
    --photo-tone-a: #8a9bb1;
    --photo-tone-b: #c9a58a;
    --text-white: #ffffff;
  }
  * { box-sizing: border-box; margin: 0; padding: 0; }
  html, body { width: 1200px; height: 850px; overflow: hidden; }
  body {
    background: var(--page-bg);
    font-family: "Cinzel", serif;
    position: relative;
  }
  .card {
    position: absolute;
    width: 532px;
    height: 302px;
    background: var(--card-white);
    box-shadow: 0 4px 14px rgba(0,0,0,0.25);
    overflow: hidden;
  }
  .card--front { left: 58px; top: 154px; }
  .card--back-navy { left: 596px; top: 154px; }
  .card--back-white { left: 334px; top: 492px; }

  /* Front */
  .portrait {
    position: absolute; left: 19px; top: 19px; width: 96px; height: 134px;
    background: linear-gradient(160deg, var(--photo-tone-a), var(--photo-tone-b));
  }
  .agency-mark {
    position: absolute; left: 352px; top: 24px; width: 170px; text-align: center;
    color: var(--navy);
  }
  .agency-mark__dot {
    width: 84px; height: 84px; border-radius: 50%;
    background: var(--brand-green); margin: 0 auto 6px;
  }
  .agency-mark__name { font-size: 19px; font-weight: 600; letter-spacing: 0.3px; white-space: nowrap; }
  .agency-mark__sub { font-size: 7.5px; font-weight: 600; letter-spacing: 1px; margin-top: 1px; }
  .name-band {
    position: absolute; left: 0; top: 185px; width: 100%; height: 33px;
    background: linear-gradient(180deg, var(--band-grey), var(--band-grey-dark));
    color: var(--text-white); display: flex; align-items: center; padding-left: 38px;
  }
  .name-band__name { font-size: 18px; margin-right: 22px; }
  .name-band__title { font-size: 12px; letter-spacing: 0.5px; }
  .contact-panel {
    position: absolute; left: 0; top: 218px; width: 100%; height: 84px;
    background: var(--navy); color: var(--text-white);
    padding: 6px 0 0 36px; font-size: 11px;
  }
  .contact-row { display: flex; align-items: center; height: 23px; }
  .contact-item { display: flex; align-items: center; }
  .contact-item + .contact-item { margin-left: 22px; }
  .contact-icon { width: 14px; height: 14px; margin-right: 6px; flex: none; }

  /* Backs */
  .back-heading {
    position: absolute; left: 20px; right: 20px; top: 30px; text-align: center;
    color: var(--navy); font-size: 14px; font-weight: 600; line-height: 19px;
  }
  .back-panel {
    position: absolute; left: 0; top: 110px; width: 100%; height: 192px; background: var(--navy);
  }
  .coverage-list {
    position: absolute; list-style: none; font-size: 11.5px; line-height: 22px; top: 124px;
  }
  .card--back-navy .coverage-list { left: 118px; color: var(--text-white); }
  .card--back-white .coverage-list { left: 110px; top: 128px; color: var(--navy); }
  .coverage-list li::before {
    content: ""; display: inline-block; width: 6px; height: 6px; border-radius: 50%;
    background: currentColor; margin-right: 10px; vertical-align: 1px;
  }
  .mini-mark {
    position: absolute; right: 10px; bottom: 12px; width: 66px; text-align: center;
    font-size: 6px; font-weight: 600; line-height: 1.2;
  }
  .mini-mark__dot {
    width: 34px; height: 34px; border-radius: 50%; background: var(--brand-green); margin: 0 auto 3px;
  }
  .card--back-navy .mini-mark { color: var(--text-white); }
  .card--back-white .mini-mark { color: var(--navy); }
</style>
</head>
<body>

<section class="card card--front">
  <div class="portrait" role="img" aria-label="Portrait photo of Marla Dempsey"></div>
  <div class="agency-mark">
    <div class="agency-mark__dot"></div>
    <div class="agency-mark__name">MARLA DEMPSEY</div>
    <div class="agency-mark__sub">INSURANCE AGENCY</div>
  </div>
  <div class="name-band">
    <span class="name-band__name">MARLA DEMPSEY</span>
    <span class="name-band__title">INDEPENDENT AGENT</span>
  </div>
  <div class="contact-panel">
    <div class="contact-row">
      <span class="contact-item">
        <svg class="contact-icon" viewBox="0 0 16 16"><circle cx="8" cy="8" r="8" fill="#fff"/><path d="M8 3.5a3 3 0 0 0-3 3c0 2.2 3 6 3 6s3-3.8 3-6a3 3 0 0 0-3-3z" fill="#1d3a64"/><circle cx="8" cy="6.5" r="1.1" fill="#fff"/></svg>
        ASHFORD, TN
      </span>
      <span class="contact-item">TOLL FREE : 888-555-0142</span>
    </div>
    <div class="contact-row">
      <span class="contact-item">
        <svg class="contact-icon" viewBox="0 0 16 16"><circle cx="8" cy="8" r="8" fill="#fff"/><path d="M5 4.2l1.6-.4 1 2.2-1 .8a5 5 0 0 0 2.6 2.6l.8-1 2.2 1-.4 1.6c-3.7.2-7-3.1-6.8-6.8z" fill="#1d3a64"/></svg>
        336-521-0974
      </span>
      <span class="contact-item">
        <svg class="contact-icon" viewBox="0 0 16 16"><circle cx="8" cy="8" r="8" fill="#fff"/><rect x="5.5" y="3.5" width="5" height="9" rx="1" fill="#1d3a64"/><rect x="6.4" y="4.6" width="3.2" height="5.6" fill="#fff"/></svg>
        336-597-2160
      </span>
    </div>
    <div class="contact-row">
      <span class="contact-item">
        <svg class="contact-icon" viewBox="0 0 16 16"><circle cx="8" cy="8" r="8" fill="#fff"/><rect x="4" y="5" width="8" height="6" fill="#1d3a64"/><path d="M4 5l4 3.2L12 5" stroke="#fff" stroke-width="0.9" fill="none"/></svg>
        MARLADEMPSEY34@QORVINMAIL.COM
      </span>
    </div>
  </div>
</section>

<section class="card card--back-navy">
  <p class="back-heading">I REPRESENT COMPANIES THAT OFFER THE PRODUCTS AND SERVICES YOU MAY NEED INORDER TO BE BETTER PREPARED FOR THE FUTURE .</p>
  <div class="back-panel"></div>
  <ul class="coverage-list">
    <li>Long-Term Care Insurance</li>
    <li>Fixed Annuities</li>
    <li>Life Insurance</li>
    <li>Medicare Supplement Insurance</li>
    <li>Individual Major Medical Insurance</li>
    <li>Final Expense Insurance</li>
    <li>Medicare Advantage Plans</li>
  </ul>
  <div class="mini-mark">
    <div class="mini-mark__dot"></div>
    MARLA DEMPSEY
  </div>
</section>

<section class="card card--back-white">
  <p class="back-heading">I REPRESENT COMPANIES THAT OFFER THE PRODUCTS AND SERVICES YOU MAY NEED INORDER TO BE BETTER PREPARED FOR THE FUTURE .</p>
  <ul class="coverage-list">
    <li>Long-Term Care Insurance</li>
    <li>Fixed Annuities</li>
    <li>Life Insurance</li>
    <li>Medicare Supplement Insurance</li>
    <li>Individual Major Medical Insurance</li>
    <li>Final Expense Insurance</li>
    <li>Medicare Advantage Plans</li>
  </ul>
  <div class="mini-mark">
    <div class="mini-mark__dot"></div>
    MARLA DEMPSEY
  </div>
</section>

</body>
</html>
```